Desk Allies Business Card

Contact Information for Business Card

Jaakko Virtanola
Managing Director

3/47 Darrow Lane Belmont ACT 2915

Tel: +61 02 6187 4326
Mob: +61 0432 715 649

Email: jaakko@deskallies-example.com.au
Web: www.deskallies-example.com.au

Colors

Designer to choose colors to be used in the design.

Requirements
Must have
• Logo, Name, Title, Address, Telephone, Mobile, Email Address and Website
• "Desk Ally Worldwide Pty Ltd"

```html
<!DOCTYPE html>
<html lang="en">
<head>
<meta charset="utf-8">
<title>Desk Allies Business Card</title>
<link href="https://fonts.googleapis.com/css2?family=Barlow+Semi+Condensed:wght@400;500;600&display=swap" rel="stylesheet">
<style>
  :root {
    --page: #e6e8eb;
    --card: #f4f4f4;
    --blue: #2b7bc4;
    --ink: #3a3a3c;
    --muted: #6a6a6e;
    --white: #ffffff;
  }
  * { box-sizing: border-box; margin: 0; padding: 0; }
  html, body { width: 1200px; height: 1200px; overflow: hidden; }
  body {
    background: var(--page);
    font-family: "Barlow Semi Condensed", Arial, sans-serif;
    color: var(--ink);
    position: relative;
  }
  .card {
    position: absolute;
    left: 160px;
    width: 880px;
    height: 503px;
    background: var(--card);
    box-shadow: 0 6px 20px rgba(0,0,0,0.12);
  }
  .card--front { top: 60px; }
  .card--back { top: 637px; }
  .frame {
    position: absolute;
    inset: 34px;
    border: 3px solid var(--blue);
    border-radius: 26px;
  }
  .name-band {
    position: absolute;
    left: 34px;
    right: 34px;
    top: 96px;
    height: 132px;
    background: var(--blue);
    color: var(--white);
    padding: 38px 0 0 44px;
  }
  .name-band__name {
    font-size: 34px;
    font-weight: 500;
    letter-spacing: 2px;
    text-transform: uppercase;
  }
  .name-band__title {
    margin-top: 6px;
    font-size: 16px;
    letter-spacing: 1px;
    text-transform: uppercase;
  }
  .contact-list {
    position: absolute;
    left: 80px;
    bottom: 62px;
    list-style: none;
  }
  .contact-list__item {
    display: flex;
    align-items: center;
    gap: 14px;
    font-size: 19px;
    line-height: 1;
    margin-top: 8px;
  }
  .contact-list__key {
    width: 22px;
    height: 22px;
    background: var(--blue);
    color: var(--white);
    font-size: 14px;
    font-weight: 600;
    display: flex;
    align-items: center;
    justify-content: center;
    border-radius: 3px;
  }
  .brand {
    position: absolute;
    display: flex;
    align-items: center;
    gap: 16px;
  }
  .brand__dot {
    border-radius: 50%;
    background: var(--blue);
    flex: none;
  }
  .brand__name {
    font-weight: 600;
    color: var(--ink);
    text-transform: uppercase;
    letter-spacing: 2px;
  }
  .card--front .brand { right: 90px; top: 270px; flex-direction: column; gap: 12px; }
  .card--front .brand__dot { width: 120px; height: 120px; }
  .card--front .brand__name { font-size: 22px; }
  .card--back .brand { left: 150px; top: 200px; }
  .card--back .brand__dot { width: 78px; height: 78px; }
  .card--back .brand__name { display: block; font-size: 52px; line-height: 1; }
  .brand__tagline {
    display: block;
    font-size: 20px;
    font-weight: 500;
    letter-spacing: 3px;
    text-transform: uppercase;
    color: var(--ink);
    margin-top: 6px;
  }
  .legal-name {
    position: absolute;
    left: 0;
    right: 0;
    bottom: 62px;
    text-align: center;
    font-size: 16px;
    font-weight: 400;
    letter-spacing: 1px;
    color: var(--muted);
  }
</style>
</head>
<body>
  <section class="card card--front">
    <div class="frame"></div>
    <div class="name-band">
      <p class="name-band__name">Jaakko Virtanola</p>
      <p class="name-band__title">Managing Director</p>
    </div>
    <div class="brand">
      <span class="brand__dot"></span>
      <span class="brand__name">Desk Allies</span>
    </div>
    <ul class="contact-list">
      <li class="contact-list__item"><span class="contact-list__key">T</span>+61 02 6187 4326</li>
      <li class="contact-list__item"><span class="contact-list__key">M</span>+61 0432 715 649</li>
      <li class="contact-list__item"><span class="contact-list__key">E</span>jaakko@deskallies-example.com.au</li>
      <li class="contact-list__item"><span class="contact-list__key">W</span>deskallies-example.com.au</li>
      <li class="contact-list__item"><span class="contact-list__key">A</span>3/47 Darrow Lane Belmont ACT 2915</li>
    </ul>
  </section>

  <section class="card card--back">
    <div class="frame"></div>
    <div class="brand">
      <span class="brand__dot"></span>
      <div>
        <span class="brand__name">Desk Allies</span>
        <span class="brand__tagline">Ergonomic Office Environments</span>
      </div>
    </div>
    <p class="legal-name">Desk Ally Worldwide Pty Ltd</p>
  </section>
</body>
</html>
```